Lena Corvell Business Card

I need a business card that reflects my current website: itslenacorvell.example and screenshot attached. If we keep the color scheme of the site and sample card below that would be ideal. The business card should include the information on the attached sample cards.

Industry/Entity Type

Business

```html
<!DOCTYPE html>
<html lang="en">
<head>
<meta charset="utf-8">
<title>Lena Corvell Business Card</title>
<link rel="stylesheet" href="https://fonts.googleapis.com/css2?family=Open+Sans:wght@400;600&family=PT+Sans+Narrow&display=swap">
<style>
  :root {
    --page: #ece9e6;
    --card: #ffffff;
    --ink: #141414;
    --teal: #6cc3b3;
    --text-grey: #6a6a6a;
    --back-grey-light: #cfcfcf;
    --back-grey-dark: #b4b4b4;
    --photo-warm: #8a6a58;
    --photo-denim: #7f9fbf;
    --white: #ffffff;
  }
  * { box-sizing: border-box; margin: 0; padding: 0; }
  html, body { width: 1200px; height: 1200px; overflow: hidden; }
  body {
    position: relative;
    background: var(--page);
    font-family: "Open Sans", sans-serif;
  }
  .card {
    position: absolute;
    box-shadow: 0 3px 10px rgba(0,0,0,.18);
  }
  .card-front {
    left: 80px; top: 90px; width: 756px; height: 466px;
    background: var(--card);
  }
  .wordmark {
    position: absolute; left: 52px; top: 150px;
    font-family: "Open Sans", sans-serif; font-weight: 600;
    font-size: 72px; color: var(--ink); letter-spacing: -1px;
    line-height: 1; white-space: nowrap;
  }
  .role-band {
    position: absolute; left: 0; top: 266px; width: 100%; height: 53px;
    background: var(--teal);
    display: flex; align-items: center; padding-left: 48px;
    font-family: "PT Sans Narrow", sans-serif; font-size: 20px;
    color: var(--white);
  }
  .role-band .divider { margin: 0 12px; }
  .contact-list {
    position: absolute; top: 349px; list-style: none;
    font-size: 17px; color: var(--text-grey); line-height: 22.5px;
    white-space: nowrap;
  }
  .contact-list li { display: flex; align-items: center; }
  .contact-list svg { width: 18px; height: 18px; margin-right: 9px; flex: none; }
  .contact-direct { left: 46px; }
  .contact-online { left: 389px; }

  .card-back {
    left: 305px; top: 578px; width: 765px; height: 475px;
    background: radial-gradient(ellipse at 40% 45%, var(--back-grey-light), var(--back-grey-dark));
    overflow: hidden;
  }
  .back-wordmark {
    position: absolute; left: 30px; top: 215px;
    font-weight: 600; font-size: 64px; color: var(--white);
    letter-spacing: -1px; line-height: 1; white-space: nowrap;
  }
  .portrait {
    position: absolute; right: 0; bottom: 0; width: 305px; height: 430px;
    background: linear-gradient(180deg, var(--photo-warm) 0%, var(--photo-warm) 55%, var(--photo-denim) 75%, var(--photo-denim) 100%);
    border-radius: 140px 140px 0 0;
    opacity: .85;
  }
</style>
</head>
<body>
  <section class="card card-front" aria-label="Card front">
    <div class="wordmark">Lena Corvell</div>
    <div class="role-band">
      <span>Brand Curator</span><span class="divider">|</span>
      <span>Digital Storyteller</span><span class="divider">|</span>
      <span>Social Entrpreneur</span>
    </div>
    <ul class="contact-list contact-direct">
      <li>
        <svg viewBox="0 0 18 18"><circle cx="9" cy="9" r="8" fill="none" stroke="#6cc3b3" stroke-width="1.5"/><path d="M5.5 6.5c0 3 3 6 6 6l1-1.5-2-1-1 .8c-1-.5-2-1.5-2.5-2.5l.8-1-1-2z" fill="#6cc3b3"/></svg>
        555.010.4471
      </li>
      <li>
        <svg viewBox="0 0 18 18"><circle cx="9" cy="9" r="8" fill="none" stroke="#6cc3b3" stroke-width="1.5"/><rect x="5" y="6" width="8" height="6" fill="none" stroke="#6cc3b3" stroke-width="1.2"/><path d="M5 6l4 3.5L13 6" fill="none" stroke="#6cc3b3" stroke-width="1.2"/></svg>
        me@lenacorvell.example
      </li>
      <li>
        <svg viewBox="0 0 18 18"><circle cx="9" cy="9" r="8" fill="none" stroke="#6cc3b3" stroke-width="1.5"/><circle cx="9" cy="9" r="4.5" fill="none" stroke="#6cc3b3" stroke-width="1"/><path d="M4.5 9h9M9 4.5v9" stroke="#6cc3b3" stroke-width="1"/></svg>
        www.itslenacorvell.example
      </li>
    </ul>
    <ul class="contact-list contact-online">
      <li><svg viewBox="0 0 18 18"><circle cx="9" cy="9" r="8" fill="none" stroke="#6cc3b3" stroke-width="1.5"/></svg>www.lenacorvell.example/social</li>
      <li><svg viewBox="0 0 18 18"><circle cx="9" cy="9" r="8" fill="none" stroke="#6cc3b3" stroke-width="1.5"/></svg>www.lenacorvell.example/updates</li>
      <li><svg viewBox="0 0 18 18"><circle cx="9" cy="9" r="8" fill="none" stroke="#6cc3b3" stroke-width="1.5"/></svg>www.lenacorvell.example/photos</li>
    </ul>
  </section>

  <section class="card card-back" aria-label="Card back">
    <div class="back-wordmark">Lena Corvell</div>
    <div class="portrait" role="img" aria-label="Photo of the card owner smiling in a denim jacket, hand holding chalk"></div>
  </section>
</body>
</html>
```